8.5 x 8.5 Dale Morven Flyer

Wednesday Workouts
with
Dale Morven
@liftwithdalemorven
Sponsored by BRAMBLE CREST HOMES GROUP
Join us Virtually each Wednesday from 7 - 7:30 pm
email frontdesk@bramblecresthomes.example for Vidora Link
reserved for BCHG Agents and Special Invitees
BRAMBLE CREST HOMES
Phone (555) 618-2739

```html
<!DOCTYPE html>
<html lang="en">
<head>
<meta charset="utf-8">
<title>Wednesday Workouts with Dale Morven</title>
<link href="https://fonts.googleapis.com/css2?family=Anton&family=Oswald:wght@500;600&family=Roboto+Condensed:wght@400;500&family=Source+Sans+3:wght@600&display=swap" rel="stylesheet">
<style>
  :root {
    --ink: #141414;
    --frame: #0d0d0d;
    --paper: #ffffff;
    --teal: #1a8f96;
    --photo-light: #e6e6e6;
    --photo-mid: #a9a9a9;
    --photo-dark: #3a3a3a;
  }
  * { margin: 0; padding: 0; box-sizing: border-box; }
  html, body { width: 1200px; height: 1200px; overflow: hidden; background: var(--frame); }
  .flyer { position: relative; width: 1200px; height: 1200px; background: var(--frame); }
  .flyer-paper {
    position: absolute; left: 30px; top: 28px; right: 30px; bottom: 28px;
    background: var(--paper); overflow: hidden;
  }
  .trainer-photo {
    position: absolute; left: 373px; top: 190px; right: 0; bottom: 0;
    background:
      linear-gradient(90deg, var(--paper) 0%, rgba(255,255,255,0) 28%),
      radial-gradient(ellipse 38% 55% at 62% 58%, var(--photo-dark) 0%, rgba(58,58,58,0) 100%),
      linear-gradient(180deg, var(--photo-light) 0%, var(--photo-mid) 60%, #8c8c8c 100%);
  }
  .copy { position: absolute; left: 73px; top: 0; width: 640px; color: var(--ink); }
  .title {
    position: absolute; left: 73px; top: 52px;
    font-family: "Anton", sans-serif; font-size: 100px; line-height: 1;
    letter-spacing: 3px; color: var(--ink); white-space: nowrap;
  }
  .host {
    position: absolute; top: 175px; left: 0;
    font-family: "Oswald", sans-serif; font-weight: 600; font-size: 62px;
    line-height: 1; color: var(--teal); font-variant: small-caps; text-transform: lowercase;
    white-space: nowrap;
  }
  .host::first-letter { text-transform: uppercase; }
  .handle {
    position: absolute; top: 262px; left: 0;
    font-family: "Source Sans 3", sans-serif; font-weight: 600; font-size: 40px; line-height: 1;
  }
  .label {
    font-family: "Oswald", sans-serif; font-weight: 600; color: var(--teal);
  }
  .join-heading { position: absolute; top: 405px; left: 0; font-size: 44px; line-height: 1; text-transform: uppercase; }
  .detail {
    font-family: "Roboto Condensed", sans-serif; font-weight: 400; font-size: 34px;
    line-height: 42px; white-space: nowrap;
  }
  .detail .label { font-family: "Roboto Condensed", sans-serif; font-weight: 500; }
  .schedule { position: absolute; top: 468px; left: 0; text-transform: uppercase; }
  .contact { position: absolute; top: 585px; left: 0; }
  .reserved-heading {
    position: absolute; top: 758px; left: 0;
    font-family: "Roboto Condensed", sans-serif; font-weight: 500; font-size: 34px;
    line-height: 1; color: var(--teal); text-transform: uppercase;
  }
  .reserved { position: absolute; top: 802px; left: 0; }
  .sponsor { position: absolute; top: 920px; left: 0; display: flex; align-items: flex-end; gap: 22px; }
  .sponsor-lead {
    font-family: "Roboto Condensed", sans-serif; font-weight: 500; font-size: 22px;
    letter-spacing: 1px; text-transform: uppercase; padding-bottom: 2px;
  }
  .sponsor-name {
    display: flex; align-items: center; gap: 10px;
    font-family: "Roboto Condensed", sans-serif; font-weight: 500; font-size: 24px;
    color: var(--teal); text-transform: uppercase; white-space: nowrap;
  }
  .sponsor-name .mark { width: 22px; height: 22px; background: var(--teal); }
  .phone {
    position: absolute; top: 1058px; left: 0;
    font-family: "Oswald", sans-serif; font-weight: 500; font-size: 42px; line-height: 1; white-space: nowrap;
  }
  .phone .label { font-variant: small-caps; text-transform: lowercase; }
  .phone .label::first-letter { text-transform: uppercase; }
</style>
</head>
<body>
  <main class="flyer">
    <section class="flyer-paper">
      <div class="trainer-photo" role="img" aria-label="Photo of the trainer crouching in a gym with a hand resting on a medicine ball"></div>

      <h1 class="title">WEDNESDAY WORKOUTS</h1>

      <div class="copy">
        <h2 class="host">With Dale Morven</h2>
        <p class="handle">@liftwithdalemorven</p>

        <h3 class="label join-heading">Join Us</h3>
        <p class="detail schedule">Virtually each<br><span class="label">Wednesday</span> from 7 - 7:30 pm</p>

        <p class="detail contact"><span class="label">EMAIL</span> frontdesk@bramblecresthomes.example<br>for Vidora Link</p>

        <h3 class="reserved-heading">Reserved for</h3>
        <p class="detail reserved">BCHG Agents and Special Invitees</p>

        <div class="sponsor">
          <span class="sponsor-lead">Sponsored by</span>
          <span class="sponsor-name"><span class="mark"></span>Bramble Crest Homes</span>
        </div>

        <p class="phone"><span class="label">Phone</span> (555) 618-2739</p>
      </div>
    </section>
  </main>
</body>
</html>
```